We are a Leadership Specialist Boutique Business that is launching a residential womans workshop....

We need a post card which will include our logo, an overview of our workshop, a catch statement on one side and on the other side dates, venue, facilitators and contacts to book the workshop. The postcards will be distributed at an Global Sisterhood Harvest Lunch. They will be placed at each setting of the lunch attendees. The company QBR running the lunch is a sponsor of our business.

Target Market(s)

Women supervisor to middle management positions or own business

Industry/Entity Type

Academic Training

Font styles to use
Serif

Colors
34a7d8

Requirements
Must have
• Use Colour Palette on docs attached, Logo, Workshop overview either the Circle Theory or the Core Philosophy Text,
• The dates, venue, all costs of the program including discount code. One catch sentence that grabs the audience from the content I have provided that appeals to the designer
• Must have these contacts.
• Website: brightpathforwardgroup.com,au
• Email: Info@brightpathforwardgroup.com.au.
• Phone: 0419372605
Nice to have
• Facilitators Photos and names

```html
<!DOCTYPE html>
<html lang="en">
<head>
<meta charset="utf-8">
<title>BrightPath Residential Program Postcard</title>
<link rel="stylesheet" href="https://fonts.googleapis.com/css2?family=Raleway:ital,wght@0,400;0,500;0,600;0,700;1,400;1,500&family=Lato:wght@400;700;900&family=Damion&display=swap">
<style>
  :root{
    --stage:#6e6e6e;
    --mint:#a9e1d6;
    --mint-deep:#7dd0bf;
    --teal-text:#3aa891;
    --navy:#16163f;
    --ink:#1b1b1b;
    --white:#ffffff;
    --grey-text:#555;
    --black:#0c0c0c;
  }
  *{box-sizing:border-box;margin:0;padding:0}
  html,body{width:902px;height:1200px;overflow:hidden;background:var(--stage)}
  body{position:relative;font-family:'Raleway',sans-serif;color:var(--navy)}
  .side-label{position:absolute;color:var(--white);font-family:'Lato',sans-serif;font-weight:700;font-size:26px}
  .side-label--front{left:42px;top:165px}
  .side-label--back{left:798px;top:1022px}

  .card{position:absolute;width:695px;height:496px;overflow:hidden;box-shadow:0 14px 24px rgba(0,0,0,.35)}
  .card--front{left:165px;top:80px}
  .card--back{left:42px;top:652px}
  .card__art{position:absolute;inset:0}

  /* FRONT */
  .brand{position:absolute;left:46px;top:76px;width:192px;height:192px;border:7px solid var(--ink);border-radius:50%;display:flex;align-items:center;justify-content:center}
  .brand__name{font-family:'Raleway',sans-serif;font-weight:700;font-size:31px;color:var(--ink)}
  .tagline{position:absolute;left:10px;top:312px;width:300px;text-align:center;font-family:'Damion',cursive;font-size:25px;line-height:35px;color:var(--ink)}
  .tagline__light{color:var(--white)}
  .philosophy{position:absolute;left:300px;top:50px;width:390px;text-align:center}
  .philosophy__title{font-family:'Lato',sans-serif;font-weight:900;font-size:24px;line-height:30px;color:var(--navy);letter-spacing:.3px}
  .pillar{margin-top:20px}
  .pillar + .pillar{margin-top:10px}
  .pillar__tag{display:inline-block;min-width:152px;padding:3px 12px;border:1.5px solid var(--mint-deep);border-radius:14px;font-weight:700;font-size:15px;color:var(--mint-deep);letter-spacing:.5px}
  .pillar__text{margin-top:5px;font-size:13.5px;line-height:17px;color:var(--navy)}
  .philosophy__close{margin-top:12px;font-style:italic;font-size:13.5px;line-height:17px}

  .contacts{position:absolute;color:var(--white);font-family:'Raleway',sans-serif}
  .contacts__row{display:flex;align-items:center;gap:6px}
  .contacts__row svg{flex:none}
  .contacts--front{right:12px;top:432px;text-align:right}
  .contacts--front .contacts__row{justify-content:flex-end}
  .contacts__phone{font-size:18px;letter-spacing:.4px}
  .contacts__small{font-size:11px;line-height:19px}

  /* BACK */
  .mentors__title{position:absolute;left:24px;top:22px;font-size:15.5px;color:var(--teal-text);letter-spacing:.3px}
  .mentor__photo{position:absolute;width:94px;height:94px;border-radius:50%;background:radial-gradient(circle at 50% 40%,#d9d9d9,#8a8a8a);border:3px solid var(--white);box-shadow:0 2px 4px rgba(0,0,0,.3)}
  .mentor__name{position:absolute;font-size:13.5px;color:var(--ink);letter-spacing:.3px}
  .mentor__role{position:absolute;font-size:10px;font-style:italic;line-height:13px;color:var(--grey-text)}
  .mentor__bio{position:absolute;left:20px;width:280px;font-size:8.6px;font-style:italic;line-height:11px;color:var(--grey-text)}
  .mentor__bio p + p{margin-top:5px}

  .program{position:absolute;left:318px;top:36px;width:372px;text-align:center;color:var(--white)}
  .program__heading{font-size:19px;font-weight:500;letter-spacing:.3px;line-height:23px}
  .program__rule{display:flex;align-items:center;gap:8px;justify-content:center}
  .program__rule::before,.program__rule::after{content:"";flex:1;height:1px;background:var(--white)}
  .dates{display:flex;justify-content:space-between;margin-top:10px;color:var(--ink);font-size:10.5px;line-height:12.5px;padding:0 4px}
  .dates__col{width:33%}
  .dates__big{font-family:'Lato',sans-serif;font-weight:900;font-size:16px;line-height:19px}
  .dates__bold{font-weight:700;font-size:10px}
  .program__body{color:var(--ink);font-size:12px;line-height:15px;margin-top:3px}
  .program__body--small{font-size:11px;line-height:14px}
  .program__block{margin-top:9px}
  .invest{position:absolute;left:365px;top:336px;width:200px;text-align:center}
  .invest__heading{font-size:15px;line-height:18px;color:var(--white);font-weight:500}
  .invest__price{font-family:'Lato',sans-serif;font-size:15px;line-height:18px;color:var(--ink);margin-top:5px}
  .invest__price b{font-weight:900}
  .discount{position:absolute;left:566px;top:339px;width:104px;height:104px;border-radius:50%;background:var(--white);border:2px dotted var(--ink);display:flex;flex-direction:column;align-items:center;justify-content:center;text-align:center;font-family:'Lato',sans-serif;font-weight:700;color:var(--ink);line-height:14px}
  .discount__small{font-size:10.5px}
  .discount__big{font-size:13px;font-weight:900}
  .contacts--back{left:36px;top:428px}
</style>
</head>
<body>

<div class="side-label side-label--front">Front</div>
<div class="side-label side-label--back">Back</div>

<!-- FRONT SIDE -->
<section class="card card--front">
  <svg class="card__art" width="695" height="496" viewBox="0 0 695 496">
    <defs>
      <linearGradient id="frontBand" x1="0" x2="1" y1="0" y2="0">
        <stop offset="0" stop-color="#050505"/>
        <stop offset=".45" stop-color="#1a1a1a"/>
        <stop offset=".68" stop-color="#8a8a8a"/>
        <stop offset=".85" stop-color="#1a1a1a"/>
        <stop offset="1" stop-color="#050505"/>
      </linearGradient>
    </defs>
    <rect width="695" height="496" fill="#a9e1d6" role="img" aria-label="Faint botanical leaf pattern and a woman's profile silhouette in mint tones"/>
    <path d="M372,0 H695 V410 C560,392 420,372 300,376 C290,320 268,250 292,190 C310,130 330,60 372,0 Z" fill="#ffffff"/>
    <path d="M0,448 C220,470 470,430 695,388 V400 C470,442 220,482 0,462 Z" fill="#ffffff"/>
    <path d="M0,446 C220,468 470,426 695,386" fill="none" stroke="#7dd0bf" stroke-width="1.5"/>
    <path d="M0,462 C220,482 470,442 695,400 V496 H0 Z" fill="url(#frontBand)"/>
  </svg>

  <div class="brand"><span class="brand__name">BrightPath</span></div>

  <p class="tagline">
    A Residential Program<br>
    <span class="tagline__light">Enhancing your</span><br>
    leadership skills, life balance<br>
    and wellbeing.
  </p>

  <div class="philosophy">
    <h1 class="philosophy__title">THE CORE PHILOSOPHY OF<br>THE PROGRAM</h1>
    <div class="pillar">
      <span class="pillar__tag">WORLDVIEW</span>
      <p class="pillar__text">A view held inside of us as to how things work.</p>
    </div>
    <div class="pillar">
      <span class="pillar__tag">BIASES</span>
      <p class="pillar__text">Our own behaviours and the behaviours of others that<br>reinforce these worldviews.</p>
    </div>
    <div class="pillar">
      <span class="pillar__tag">ERROR SCRIPTS</span>
      <p class="pillar__text">Stories implanted by us or others that limits our potential</p>
    </div>
    <p class="philosophy__close">Rewriting a new Personal Narrative allows us to shatter our<br>own glass celing</p>
  </div>

  <div class="contacts contacts--front">
    <div class="contacts__row contacts__phone">0419372605
      <svg width="16" height="16" viewBox="0 0 16 16"><circle cx="8" cy="8" r="7" fill="none" stroke="#fff" stroke-width="1.2"/><path d="M5.5,4.5 L7,6.5 L6.3,7.3 C6.8,8.5 7.6,9.3 8.7,9.8 L9.5,9 L11.5,10.5 L10.5,11.8 C7.5,11.5 4.6,8.6 4.3,5.5 Z" fill="#fff"/></svg>
    </div>
    <div class="contacts__row contacts__small">Info@brightpathforwardgroup.com.au
      <svg width="13" height="9" viewBox="0 0 13 9"><rect x=".5" y=".5" width="12" height="8" fill="#a9e1d6"/><path d="M.5,.5 L6.5,5 L12.5,.5" fill="none" stroke="#333" stroke-width="1"/></svg>
    </div>
    <div class="contacts__row contacts__small">brightpathforwardgroup.com.au
      <svg width="12" height="12" viewBox="0 0 12 12"><circle cx="6" cy="6" r="5.3" fill="none" stroke="#a9e1d6" stroke-width="1"/><ellipse cx="6" cy="6" rx="2.3" ry="5.3" fill="none" stroke="#a9e1d6" stroke-width="1"/><path d="M.7,6 H11.3" stroke="#a9e1d6" stroke-width="1"/></svg>
    </div>
  </div>
</section>

<!-- BACK SIDE -->
<section class="card card--back">
  <svg class="card__art" width="695" height="496" viewBox="0 0 695 496">
    <defs>
      <linearGradient id="backBg" x1="0" x2="1">
        <stop offset="0" stop-color="#ffffff"/>
        <stop offset=".45" stop-color="#f7f7f7"/>
        <stop offset="1" stop-color="#cfcfcf"/>
      </linearGradient>
      <linearGradient id="backBand" x1="0" x2="1">
        <stop offset="0" stop-color="#050505"/>
        <stop offset=".25" stop-color="#111"/>
        <stop offset=".42" stop-color="#8f8f8f"/>
        <stop offset=".55" stop-color="#1a1a1a"/>
        <stop offset="1" stop-color="#050505"/>
      </linearGradient>
    </defs>
    <rect width="695" height="496" fill="url(#backBg)"/>
    <path d="M0,400 C120,402 260,420 340,450 V496 H0 Z" fill="url(#backBand)"/>
    <path d="M0,385 C120,386 260,404 340,434" fill="none" stroke="#7dd0bf" stroke-width="2"/>
    <circle cx="512" cy="250" r="268" fill="#e9e9e9"/>
    <circle cx="512" cy="250" r="260" fill="#ffffff" stroke="#d6d6d6" stroke-width="2"/>
    <circle cx="508" cy="246" r="246" fill="#7ed1bf"/>
  </svg>

  <h2 class="mentors__title">PROGRAM MENTORS AND FOUNDERS</h2>

  <div class="mentor__photo" style="left:18px;top:50px" role="img" aria-label="Portrait photo of mentor Dana Whitfield"></div>
  <h3 class="mentor__name" style="left:124px;top:80px">DANA WHITFIELD</h3>
  <p class="mentor__role" style="left:124px;top:99px">An Intuitive Advisor to<br>empowered women</p>
  <div class="mentor__bio" style="top:159px">
    <p>Dana is passionate about intuitive guidance to women in life and their careers.</p>
    <p>Dana develops and implements strategies that transform people, teams and organisations, with a particular focus on the raising of confidence and fulfilment of women by coaching them towards their life purpose.</p>
  </div>

  <div class="mentor__photo" style="left:18px;top:224px" role="img" aria-label="Portrait photo of mentor Colin Ashgrove"></div>
  <h3 class="mentor__name" style="left:124px;top:261px">COLIN ASHGROVE</h3>
  <p class="mentor__role" style="left:124px;top:280px">Trusted Advisor to wise<br>women</p>
  <div class="mentor__bio" style="top:331px">
    <p>Developing leadership styles and strategies that enable women in leadership roles to leverage their value by tapping into all their inner strengths</p>
    <p>Equipping women with behaviour change tools to embrace growth in their life and career.</p>
  </div>

  <div class="program">
    <h2 class="program__heading">PROGRAM AND UPCOMING</h2>
    <div class="program__rule program__heading">DATES</div>
    <div class="dates">
      <div class="dates__col">2 ½ Days residential<br><span class="dates__big">26th to 28th</span><br>May 2019</div>
      <div class="dates__col">May Venue<br><span class="dates__bold">The Riverbend Lodge, Hollis Vale NSW</span></div>
      <div class="dates__col">Future Programs<br><span class="dates__bold">August, October, March</span></div>
    </div>
    <div class="program__block">
      <div class="program__rule program__heading">WHY</div>
      <p class="program__body">The BrightPath Program assists you to uncover the blockers of your success by giving yourself the time to explore possibilities, in a supportive environment.</p>
    </div>
    <div class="program__block">
      <h2 class="program__heading">SUPPORT &amp; PROGRAM INCLUSIONS</h2>
      <p class="program__body program__body--small">Leadership skills workshops, Life style sessions and Assessments supported by Coaching.<br>Body Wellness Therapies including - Meditation, Yoga, Reiki, Reflexology and Massage.<br><b>Accommodation and all meals are included.</b></p>
    </div>
  </div>

  <div class="invest">
    <h2 class="invest__heading">INVESTMENT FOR<br>MAY 2019 PROGRAM</h2>
    <p class="invest__price"><b>$3,495</b><br>(Early Bird Book by<br>26th April) <b>$3,095</b></p>
  </div>

  <div class="discount">
    <span class="discount__small">Quote</span>
    <span class="discount__big">QBR Code 9455</span>
    <span class="discount__small">for a further</span>
    <span class="discount__big">$100 Discount</span>
  </div>

  <div class="contacts contacts--back">
    <div class="contacts__row contacts__phone">
      <svg width="16" height="16" viewBox="0 0 16 16"><circle cx="8" cy="8" r="7" fill="none" stroke="#fff" stroke-width="1.2"/><path d="M5.5,4.5 L7,6.5 L6.3,7.3 C6.8,8.5 7.6,9.3 8.7,9.8 L9.5,9 L11.5,10.5 L10.5,11.8 C7.5,11.5 4.6,8.6 4.3,5.5 Z" fill="#fff"/></svg>
      0419372605
    </div>
    <div class="contacts__row contacts__small">
      <svg width="13" height="9" viewBox="0 0 13 9"><rect x=".5" y=".5" width="12" height="8" fill="#a9e1d6"/><path d="M.5,.5 L6.5,5 L12.5,.5" fill="none" stroke="#333" stroke-width="1"/></svg>
      Info@brightpathforwardgroup.com.au
    </div>
    <div class="contacts__row contacts__small">
      <svg width="12" height="12" viewBox="0 0 12 12"><circle cx="6" cy="6" r="5.3" fill="none" stroke="#a9e1d6" stroke-width="1"/><ellipse cx="6" cy="6" rx="2.3" ry="5.3" fill="none" stroke="#a9e1d6" stroke-width="1"/><path d="M.7,6 H11.3" stroke="#a9e1d6" stroke-width="1"/></svg>
      brightpathforwardgroup.com.au
    </div>
  </div>
</section>

</body>
</html>
```